New Business Card Design for Engineering and Surveying Company

We need a new design template for our business cards. We are a civil engineering, land surveying and pipeline integrity business. Please see brqholt.com for details. We need a bold, new business card design to complement our rebranding and marketing program. We have anew logo and attached vectro file. Please find additional details below. I am available to answer any questions.

Target Market(s)

Contractors, business owners, oil companies

Contact Information for Business Card

Needs to be customizable for different people (name, title, cell)

Font styles to use
Sans Serif
Other font styles liked:
• See eps file

Requirements
Must have
• Example Information:
Derek Fannaby

T:418-555-0187
M: 306-555-0143
dfannaby@brqholt.com

Address: 1870 Corvane Parkway, Harlow Bend, Kestan 77701
Email: dfanbagy@brqholt.com
Website: www.brqholt.com
Nice to have
• I would like the back of the card to have the logo on a bold background with the text below:

[logo]
ROLAND FANNABY & ASSOCIATES
CIVIL ENGINEERING | LAND SURVEYING | PIPELINE INTEGRITY

The reverse side should have the contact information for the person (example above), a smaller version of the logo and a graphic

```html
<!DOCTYPE html>
<html lang="en">
<head>
<meta charset="utf-8">
<title>Roland Fannaby &amp; Associates – Business Card</title>
<link rel="stylesheet" href="https://fonts.googleapis.com/css2?family=Open+Sans:wght@400;600;700;800&display=swap">
<style>
  :root {
    --backdrop: #2a2a2c;
    --navy: #070b14;
    --ink: #0b0f1a;
    --white: #ffffff;
    --paper: #f4f4f4;
    --red: #e3202f;
    --blue: #1f4fa8;
    --muted: #1a1a1a;
  }
  * { box-sizing: border-box; margin: 0; padding: 0; }
  html, body { width: 1200px; height: 1021px; overflow: hidden; }
  body {
    background: var(--backdrop);
    font-family: "Open Sans", Arial, sans-serif;
    position: relative;
  }
  .card {
    position: absolute;
    left: 320px;
    width: 560px;
    height: 320px;
    box-shadow: 0 10px 30px rgba(0,0,0,.45);
  }
  /* Back of card */
  .card--back { top: 150px; background: var(--navy); color: var(--white); }
  .back-brand {
    position: absolute; left: 190px; top: 78px;
    display: flex; align-items: center; gap: 14px;
  }
  .brand-mark { width: 22px; height: 22px; background: var(--red); }
  .back-brand .brand-name {
    font-weight: 800; font-size: 84px; line-height: 1; letter-spacing: -2px; color: var(--white);
  }
  .back-company {
    position: absolute; left: 226px; top: 172px;
    font-weight: 700; font-size: 13px; letter-spacing: .6px;
  }
  .back-services {
    position: absolute; left: 0; right: 0; bottom: 46px;
    text-align: center; font-size: 14px; letter-spacing: .8px;
  }
  .back-services .sep { color: var(--red); margin: 0 8px; }

  /* Front of card */
  .card--front { top: 540px; background: linear-gradient(180deg, var(--white), var(--paper)); color: var(--muted); }
  .front-brand {
    position: absolute; left: 42px; top: 118px;
    display: flex; align-items: center; gap: 12px;
  }
  .front-brand .brand-name {
    font-weight: 800; font-size: 64px; line-height: 1; letter-spacing: -2px; color: var(--ink);
  }
  .front-brand .brand-mark { width: 18px; height: 18px; }
  .divider { position: absolute; left: 262px; top: 48px; width: 1.5px; height: 224px; background: var(--ink); }
  .contact { position: absolute; left: 290px; top: 50px; }
  .contact-name { color: var(--blue); font-weight: 700; font-size: 22px; line-height: 1.1; }
  .contact-title { font-size: 15px; margin-bottom: 14px; }
  .contact-address { font-size: 15px; line-height: 1.25; margin-bottom: 4px; }
  .contact-list { list-style: none; font-size: 15px; line-height: 1.35; }
  .contact-list li { display: flex; align-items: center; gap: 8px; }
  .contact-list svg { width: 13px; height: 13px; flex: none; }
</style>
</head>
<body>

<section class="card card--back" aria-label="Card back">
  <div class="back-brand">
    <span class="brand-mark"></span>
    <span class="brand-name">RFA</span>
  </div>
  <p class="back-company">ROLAND FANNABY &amp; ASSOCIATES</p>
  <p class="back-services">CIVIL ENGINEERING<span class="sep">|</span>LAND SURVEYING<span class="sep">|</span>PIPELINE INTEGRITY</p>
</section>

<section class="card card--front" aria-label="Card front">
  <div class="front-brand">
    <span class="brand-mark"></span>
    <span class="brand-name">RFA</span>
  </div>
  <div class="divider"></div>
  <div class="contact">
    <p class="contact-name">Derek Fannaby</p>
    <p class="contact-title">Founder</p>
    <p class="contact-address">1870 Corvane Parkway<br>Harlow Bend, Kestan 77701</p>
    <ul class="contact-list">
      <li>
        <svg viewBox="0 0 16 16"><path fill="#e3202f" d="M3 1l3 1 1 4-2 1c1 2 2 3 4 4l1-2 4 1 1 3-2 2C7 15 1 9 1 3z"/></svg>
        418-555-0187
      </li>
      <li>
        <svg viewBox="0 0 16 16"><rect x="4" y="1" width="8" height="14" rx="1.5" fill="none" stroke="#e3202f" stroke-width="1.6"/><circle cx="8" cy="12.5" r="1" fill="#e3202f"/></svg>
        306-555-0143
      </li>
      <li>
        <svg viewBox="0 0 16 16"><rect x="1" y="3" width="14" height="10" fill="none" stroke="#e3202f" stroke-width="1.6"/><path d="M1 3l7 6 7-6" fill="none" stroke="#e3202f" stroke-width="1.6"/></svg>
        dfannaby@brqholt.com
      </li>
      <li>
        <svg viewBox="0 0 16 16"><rect x="1" y="3" width="14" height="10" fill="none" stroke="#e3202f" stroke-width="1.6"/><path d="M1 3l7 6 7-6" fill="none" stroke="#e3202f" stroke-width="1.6"/></svg>
        dfanbagy@brqholt.com
      </li>
      <li>
        <svg viewBox="0 0 16 16"><g fill="none" stroke="#e3202f" stroke-width="1.3"><circle cx="8" cy="8" r="6.5"/><ellipse cx="8" cy="8" rx="3" ry="6.5"/><path d="M1.5 8h13M2.5 4.5h11M2.5 11.5h11"/></g></svg>
        www.brqholt.com
      </li>
    </ul>
  </div>
</section>

</body>
</html>
```